We need a complete new design for laser toner cartridge packaging box . I will upload some old design , but i want it complete deferents , i want to remove ( smart printing solutions ) from my logo Zulbenvaro , lets work on that size for now
350x100x150 mm
486x190x238 mm

I prefer orange/black/white color , also you can use pictures

```html
<!DOCTYPE html>
<html lang="en">
<head>
<meta charset="utf-8">
<title>Zulbenvaro Toner Box Dieline</title>
<link rel="stylesheet" href="https://fonts.googleapis.com/css2?family=Open+Sans:wght@300;400;600;700;800&display=swap">
<style>
  :root {
    --bg-brown: #3a2418;
    --orange: #f47421;
    --orange-light: #f89a5c;
    --white: #ffffff;
    --black: #111111;
    --flap-grey: #ececee;
    --dash-grey: #b9b9bd;
    --text-dark: #222222;
    --font-main: "Open Sans", Arial, sans-serif;
  }
  * { box-sizing: border-box; margin: 0; padding: 0; }
  html, body { width: 1000px; height: 1200px; overflow: hidden; background: var(--bg-brown); }
  body { position: relative; font-family: var(--font-main); }

  .sheet-title { position: absolute; left: 117px; top: 36px; color: var(--white); }
  .sheet-title h1 { font-weight: 300; font-size: 58px; letter-spacing: 1px; line-height: 1; }
  .sheet-title p { font-weight: 400; font-size: 33px; margin-top: 6px; }

  .panel { position: absolute; }
  .tuck-flap { left: 202px; top: 228px; width: 610px; height: 33px; background: var(--flap-grey); border-radius: 12px 12px 0 0; border-bottom: 1px solid #d4d4d8; }
  .lid-inner { left: 202px; top: 261px; width: 610px; height: 261px; background: var(--flap-grey); }
  .lid-inner svg { width: 100%; height: 100%; display: block; }

  .top-face { left: 202px; top: 522px; width: 610px; height: 105px; background: var(--white); }
  .top-face .flipped { position: absolute; inset: 0; transform: rotate(180deg); }
  .top-face .headline { position: absolute; left: 72px; top: 20px; line-height: 1.08; }
  .top-face .headline .accent { color: var(--orange); font-size: 24px; font-weight: 600; }
  .top-face .headline .strong { color: var(--black); font-size: 24px; font-weight: 800; }
  .top-face .tagline { position: absolute; right: 16px; top: 14px; font-size: 15px; color: var(--black); letter-spacing: 0.3px; }
  .top-face .tagline b { font-weight: 800; }
  .top-face .code-caption { position: absolute; right: 52px; top: 82px; font-size: 6px; color: var(--black); }
  .band-black { left: 202px; top: 627px; width: 610px; height: 13px; background: var(--black); }

  .front-lip { left: 202px; top: 640px; width: 610px; height: 58px; background: var(--orange); }

  .front-face { left: 202px; top: 698px; width: 610px; height: 260px; background: var(--orange); overflow: hidden; }
  .bottom-face { left: 202px; top: 958px; width: 610px; height: 175px; background: var(--orange); overflow: hidden; }
  .light-half { position: absolute; left: 0; top: 0; width: 283px; height: 100%; background: var(--white); }

  .pattern-zone { position: absolute; }
  .front-face .pattern-zone {
    left: 220px; top: 0; width: 390px; height: 260px;
    background:
      radial-gradient(ellipse 120px 90px at 110px 140px, rgba(255,255,255,0.38), rgba(255,255,255,0) 100%),
      radial-gradient(ellipse 110px 70px at 250px 200px, rgba(255,255,255,0.22), rgba(255,255,255,0) 100%),
      radial-gradient(ellipse 60px 50px at 120px 30px, rgba(255,255,255,0.2), rgba(255,255,255,0) 100%);
  }
  .bottom-face .pattern-zone {
    left: 200px; top: 0; width: 160px; height: 175px;
    background: radial-gradient(ellipse 90px 80px at 80px 60px, rgba(255,255,255,0.3), rgba(255,255,255,0) 100%);
  }

  .brand-word { font-weight: 800; letter-spacing: 0.3px; line-height: 1; display: flex; align-items: center; gap: 8px; }
  .brand-word .mark-square { width: 20px; height: 20px; background: var(--orange); display: inline-block; }
  .front-face .brand-word { position: absolute; left: 14px; top: 22px; font-size: 32px; color: var(--black); }
  .front-face .brand-word .mark-square { width: 28px; height: 28px; }
  .front-face .subbrand { position: absolute; left: 62px; top: 72px; font-size: 15px; color: var(--black); letter-spacing: 0.5px; }
  .front-face .subbrand b { font-weight: 800; }
  .product-shot { position: absolute; left: 16px; top: 98px; width: 262px; height: 104px; border-radius: 6px; background: linear-gradient(160deg, #3b3b3b 0%, #141414 60%, #2a2a2a 100%); }
  .feature-icons { position: absolute; left: 97px; top: 211px; display: flex; gap: 8px; }
  .feature-icons span { width: 26px; height: 26px; border: 1.5px solid var(--orange); border-radius: 5px; font-size: 4.5px; font-weight: 700; color: var(--orange); display: flex; align-items: center; justify-content: center; background: var(--white); }
  .front-face .headline { position: absolute; left: 342px; top: 46px; width: 250px; text-align: center; color: var(--white); line-height: 1.3; }
  .front-face .headline .line-a { font-size: 20px; font-weight: 600; }
  .front-face .headline .line-b { font-size: 21px; font-weight: 800; }

  .side-left { left: 26px; top: 698px; width: 176px; height: 260px; background: var(--orange); overflow: hidden; }
  .side-right { left: 812px; top: 698px; width: 176px; height: 260px; background: var(--orange); }
  .side-left .brand-word, .side-right .brand-word { position: absolute; left: 22px; top: 32px; font-size: 19px; color: var(--white); }
  .side-left .brand-word .mark-square, .side-right .brand-word .mark-square { background: var(--black); width: 16px; height: 16px; }
  .side-title { position: absolute; left: 0; width: 100%; text-align: center; color: var(--white); font-weight: 700; font-size: 12px; line-height: 1.25; }
  .side-left .side-title { top: 76px; }
  .side-right .side-title { top: 80px; }
  .side-copy { position: absolute; left: 22px; top: 116px; width: 134px; text-align: center; color: var(--white); font-size: 6.6px; line-height: 1.4; }
  .side-right .white-strip { position: absolute; left: 0; top: 122px; width: 100%; height: 50px; background: var(--white); }
  .side-right .strip-caption { position: absolute; left: 0; top: 160px; width: 100%; text-align: center; font-size: 6px; color: var(--black); }
  .side-left .pattern-zone {
    left: 0; top: 150px; width: 176px; height: 110px;
    background: radial-gradient(ellipse 90px 60px at 50px 80px, rgba(255,255,255,0.35), rgba(255,255,255,0) 100%);
  }

  .cert-row { position: absolute; display: flex; align-items: center; gap: 10px; }
  .cert-row .cert-circle { width: 28px; height: 28px; border-radius: 50%; }
  .cert-row .cert-square { width: 24px; height: 24px; border-radius: 4px; }
  .side-right .cert-row { left: 32px; top: 206px; }
  .side-right .cert-row span { background: var(--white); }

  .bottom-face .brand-word { position: absolute; left: 18px; top: 24px; font-size: 22px; color: var(--black); }
  .bottom-face .motto { position: absolute; left: 18px; top: 66px; font-size: 10px; color: var(--text-dark); line-height: 1.4; }
  .bottom-face .cert-row { left: 20px; top: 130px; }
  .bottom-face .cert-row span { background: var(--black); }
  .drum-art { position: absolute; left: 378px; top: 26px; width: 176px; height: 92px; border-radius: 6px; background: linear-gradient(135deg, rgba(255,255,255,0.32), rgba(255,255,255,0.1)); }
  .bottom-face .info-title { position: absolute; left: 328px; top: 130px; color: var(--white); font-size: 11px; font-weight: 700; }
  .bottom-face .info-copy { position: absolute; left: 328px; top: 147px; width: 240px; color: var(--white); font-size: 6.2px; line-height: 1.3; }
</style>
</head>
<body>
  <header class="sheet-title">
    <h1>PACKAGE</h1>
    <p>350x100x150 mm</p>
  </header>

  <div class="panel tuck-flap"></div>
  <div class="panel lid-inner">
    <svg viewBox="0 0 610 261" preserveAspectRatio="none" aria-hidden="true">
      <line x1="0" y1="0" x2="610" y2="261" stroke="var(--dash-grey)" stroke-dasharray="6 4" stroke-width="1"/>
      <line x1="610" y1="0" x2="0" y2="261" stroke="var(--dash-grey)" stroke-dasharray="6 4" stroke-width="1"/>
    </svg>
  </div>

  <section class="panel top-face">
    <div class="flipped">
      <div class="headline">
        <div class="accent">PREMIUM TONER</div>
        <div class="strong">CARTRIDGE</div>
      </div>
      <div class="tagline">PRINT <b>CARTRIDGE</b></div>
      <div class="code-caption">Zulbenvaro</div>
    </div>
  </section>
  <div class="panel band-black"></div>
  <div class="panel front-lip"></div>

  <section class="panel side-left">
    <div class="pattern-zone" role="img" aria-label="Scattered white diamond pattern"></div>
    <div class="brand-word"><span class="mark-square"></span>Zulbenvaro</div>
    <div class="side-title">PREMIUM TONER<br>CARTRIDGE</div>
    <p class="side-copy">Laser toner built for sharp, even prints on every page. Easy to fit, clean to handle, made for long office runs.</p>
  </section>

  <section class="panel front-face">
    <div class="light-half"></div>
    <div class="pattern-zone" role="img" aria-label="Scattered orange and white diamond pattern across the colour split"></div>
    <div class="brand-word"><span class="mark-square"></span>Zulbenvaro</div>
    <div class="subbrand">PRINT <b>CARTRIDGE</b></div>
    <div class="product-shot" role="img" aria-label="Photo of a black laser toner cartridge"></div>
    <div class="feature-icons"><span>ICON1</span><span>ICON2</span><span>ICON3</span></div>
    <div class="headline">
      <div class="line-a">PREMIUM TONER</div>
      <div class="line-b">CARTRIDGE</div>
    </div>
  </section>

  <section class="panel side-right">
    <div class="brand-word"><span class="mark-square"></span>Zulbenvaro</div>
    <div class="side-title">PREMIUM TONER<br>CARTRIDGE</div>
    <div class="white-strip"></div>
    <div class="strip-caption">Zulbenvaro</div>
    <div class="cert-row"><span class="cert-circle"></span><span class="cert-square"></span><span class="cert-circle"></span></div>
  </section>

  <section class="panel bottom-face">
    <div class="light-half"></div>
    <div class="pattern-zone" role="img" aria-label="Scattered orange and white diamond pattern"></div>
    <div class="brand-word"><span class="mark-square"></span>Zulbenvaro</div>
    <p class="motto">Precise.Reliable.<br>Original cartridge Toners</p>
    <div class="cert-row"><span class="cert-circle"></span><span class="cert-square"></span><span class="cert-circle"></span></div>
    <div class="drum-art" role="img" aria-label="White line drawing of a printer drum unit"></div>
    <div class="info-title">PREMIUM TONER</div>
    <p class="info-copy">Consistent density and crisp edges for everyday office printing, page after page.</p>
  </section>
</body>
</html>
```